Verdanix Medical Business Card

Create a high class Business card for Medical Aesthetics and Wellness Practice called Verdanix Medical Aesthetics and Wellness as per the logo attached.
Addresss is: 418 Harlan Brook Road Suite 312 Melville, New York 11093
Phone (555)204-7391 IG @verdanix_medical
Verdanixmedical.example

I need 5 different name configurations
1) Dr. Theo Valcourt
Aesthetics and Wellness Specialist
Medical Director

2) Rosalind Pettinger, NP
Clinical Nurse Manager

3) Marla Vostrik, RN
Aesthetic Nurse Specialist

4) Petra Halvesen, RN

5) Dana Kowbeck, L.E.
Senior Licensed Esthetician

Target Market(s)

22-55 Females

Industry/Entity Type

Medical Spa and Wellness

Contact Information for Business Card

Logo, address, phone, web, instagram, providers name

Requirements
Must have
• Attractive classy modern look

```html
<!DOCTYPE html>
<html lang="en">
<head>
<meta charset="utf-8">
<title>Verdanix Medical Business Card</title>
<link rel="stylesheet" href="https://fonts.googleapis.com/css2?family=Cormorant+Garamond:wght@500&family=Arimo:wght@400&display=swap">
<style>
  :root {
    --page-bg: #1b1b1d;
    --card-bg: #3b3b3d;
    --card-edge: #2e5a66;
    --ink: #f2f2f2;
    --ink-soft: #d6d6d6;
    --rule: #bdbdbd;
  }
  * { margin: 0; padding: 0; box-sizing: border-box; }
  html, body {
    width: 1200px; height: 874px; overflow: hidden;
    background: var(--page-bg);
  }
  .canvas {
    position: relative; width: 1200px; height: 874px;
    display: flex; flex-direction: column; align-items: center; justify-content: center; gap: 56px;
  }
  .card {
    position: relative; width: 640px; height: 366px;
    background: var(--card-bg);
    border-radius: 22px;
    box-shadow: 0 3px 0 var(--card-edge), 0 18px 40px rgba(0,0,0,0.55);
    color: var(--ink);
  }
  .wordmark {
    font-family: "Cormorant Garamond", serif;
    font-weight: 500;
    color: var(--ink);
    text-align: center;
    letter-spacing: 0.04em;
    line-height: 1.15;
  }
  .card-front { display: flex; align-items: center; justify-content: center; }
  .card-front .wordmark { font-size: 44px; width: 440px; }

  .card-back { display: flex; align-items: center; }
  .card-back .brand-block { width: 300px; display: flex; justify-content: center; }
  .card-back .wordmark { font-size: 27px; width: 250px; }
  .divider {
    width: 1.5px; height: 230px;
    background: linear-gradient(to bottom, transparent, var(--rule) 20%, var(--rule) 80%, transparent);
  }
  .contact { padding-left: 26px; font-family: "Arimo", sans-serif; color: var(--ink); }
  .person-name {
    font-family: "Cormorant Garamond", serif; font-weight: 500;
    font-size: 27px; letter-spacing: 0.02em; line-height: 1;
  }
  .person-title { font-size: 13.5px; color: var(--ink-soft); margin-top: 4px; }
  .address { font-size: 15.5px; line-height: 1.3; margin-top: 16px; }
  .links { list-style: none; margin-top: 12px; font-size: 15.5px; line-height: 1.35; }
  .links li { display: flex; align-items: center; gap: 9px; }
  .links svg { width: 13px; height: 13px; flex: none; }
</style>
</head>
<body>
  <main class="canvas">
    <section class="card card-front">
      <p class="wordmark">Verdanix Medical Aesthetics and Wellness</p>
    </section>

    <section class="card card-back">
      <div class="brand-block">
        <p class="wordmark">Verdanix Medical Aesthetics and Wellness</p>
      </div>
      <div class="divider"></div>
      <div class="contact">
        <h1 class="person-name">Rosalind Pettinger, NP</h1>
        <p class="person-title">Clinical Nurse Manager</p>
        <p class="address">418 Harlan Brook Road<br>Suite 312<br>Melville, New York 11093</p>
        <ul class="links">
          <li>
            <svg viewBox="0 0 16 16" aria-hidden="true"><path fill="#f2f2f2" d="M3.6 1.2l2.3 2.4-1.2 1.8c.8 1.9 2.1 3.2 4 4l1.8-1.2 2.4 2.3-1.5 2.3C6.8 12.5 3.5 9.2 1.2 4.6z"/></svg>
            (555)204-7391
          </li>
          <li>
            <svg viewBox="0 0 16 16" aria-hidden="true"><circle cx="8" cy="8" r="6.5" fill="none" stroke="#f2f2f2" stroke-width="1.6"/><path d="M1.5 8h13M8 1.5c-3 3.6-3 9.4 0 13M8 1.5c3 3.6 3 9.4 0 13" fill="none" stroke="#f2f2f2" stroke-width="1.2"/></svg>
            Verdanixmedical.example
          </li>
          <li>
            <svg viewBox="0 0 16 16" aria-hidden="true"><circle cx="8" cy="8" r="6.5" fill="none" stroke="#f2f2f2" stroke-width="1.6"/></svg>
            @verdanix_medical
          </li>
        </ul>
      </div>
    </section>
  </main>
</body>
</html>
```